Business card for my new company (Accounting firm)

I need a business card for my new business Corvane Advisory and Ledger SA. Our services are accounting, tax, audit and financial management. Our customers are small companies, start-ups and new companies. The final design has to show financial security, trust and growth. Please find our logo attached to the business card. Text for the business card: Corvane Advisory and Ledger SA Tomas da Varela Director and Founder Certified Accountant Tel. 022 418 27 35 tv@corvaneconseil.ch www.corvaneconseil.ch Rue des Vergers-Bleus 14 1201 Geneva
Target Market(s)
Our customers are small companies, start-ups and new companies.
Industry/Entity Type
Finance And Accounting
Contact Information for Business Card
Corvane Conseil et Registre SA
Tomas da Varela
Directeur et Fondateur
Expert-comptable diplômé
Tél. 022 418 27 35
tv@corvaneconseil.ch
www.corvaneconseil.ch
Rue des Vergers-Bleus 14
1201 Genève

```html
<!DOCTYPE html>
<html lang="fr">
<head>
<meta charset="utf-8">
<title>Corvane Conseil et Registre SA – Carte de visite</title>
<link rel="stylesheet" href="https://fonts.googleapis.com/css2?family=Open+Sans:wght@400;600&display=swap">
<style>
  :root {
    --paper: #f7f8fc;
    --blue: #0392d1;
    --blue-deep: #0071bb;
    --name-blue: #2083bf;
    --ink: #3d3d3d;
    --white: #ffffff;
  }
  html, body {
    margin: 0;
    padding: 0;
    width: 1200px;
    height: 696px;
    overflow: hidden;
    background: var(--paper);
  }
  .card {
    position: relative;
    width: 1200px;
    height: 696px;
    background: var(--paper);
    font-family: "Open Sans", Arial, sans-serif;
    overflow: hidden;
  }
  .bands {
    position: absolute;
    inset: 0;
  }
  .band-light { fill: var(--blue); }
  .band-deep { fill: var(--blue-deep); }

  .holder-name {
    position: absolute;
    left: 78px;
    top: 156px;
    margin: 0;
    font-size: 74px;
    font-weight: 600;
    letter-spacing: 0.07em;
    color: var(--name-blue);
    line-height: 1;
    white-space: nowrap;
  }

  .brand {
    position: absolute;
    left: 860px;
    top: 150px;
    width: 320px;
    text-align: center;
  }
  .brand-mark {
    display: block;
    width: 70px;
    height: 70px;
    margin: 0 auto 26px;
    background: var(--name-blue);
  }
  .brand-name {
    margin: 0;
    font-size: 38px;
    font-weight: 600;
    line-height: 1.18;
    color: var(--ink);
    letter-spacing: 0.02em;
  }

  .contacts {
    position: absolute;
    left: 0;
    top: 0;
    margin: 0;
    padding: 0;
    list-style: none;
  }
  .contact {
    position: absolute;
    left: 78px;
    display: flex;
    align-items: center;
    white-space: nowrap;
    color: var(--white);
    font-size: 36px;
    font-weight: 400;
  }
  .contact .icon {
    width: 48px;
    height: 48px;
    flex: none;
  }
  .contact .value { position: absolute; left: 83px; }
  .contact.phone { top: 348px; }
  .contact.web { top: 416px; }
  .contact.address { top: 485px; }
  .contact.email { top: 538px; }
  .icon-fill { fill: var(--white); }
  .icon-line { fill: none; stroke: var(--white); stroke-width: 3.5; }
</style>
</head>
<body>
<main class="card">
  <svg class="bands" width="1200" height="696" viewBox="0 0 1200 696" aria-hidden="true">
    <polygon class="band-light" points="0,0 867,0 921,63 0,63"/>
    <polygon class="band-light" points="0,330 467,330 537,409 834,409 1084,696 0,696"/>
    <polygon class="band-deep" points="0,409 537,409 696,592 0,592"/>
    <polygon class="band-deep" points="629,660 1200,660 1200,696 660,696"/>
  </svg>

  <h1 class="holder-name">Tomas da Varela</h1>

  <div class="brand">
    <span class="brand-mark" aria-hidden="true"></span>
    <p class="brand-name">Corvane Conseil et Registre SA</p>
  </div>

  <ul class="contacts">
    <li class="contact phone">
      <svg class="icon" viewBox="0 0 48 48" aria-hidden="true">
        <path class="icon-fill" d="M6 4c3-2 6-2 8 1l5 8c1 2 0 4-2 5l-3 2c2 6 7 11 13 14l2-3c1-2 3-3 5-2l8 5c3 2 3 5 1 8l-3 3c-3 3-8 3-13 0C17 39 9 31 4 20 1 14 1 9 4 6z"/>
      </svg>
      <span class="value">022 418 27 35</span>
    </li>
    <li class="contact web">
      <svg class="icon" viewBox="0 0 48 48" aria-hidden="true">
        <circle class="icon-line" cx="24" cy="24" r="20"/>
        <ellipse class="icon-line" cx="24" cy="24" rx="9" ry="15" style="stroke-width:2.5"/>
        <line class="icon-line" x1="24" y1="9" x2="24" y2="39" style="stroke-width:2.5"/>
        <line class="icon-line" x1="10" y1="18" x2="38" y2="18" style="stroke-width:2.5"/>
        <line class="icon-line" x1="9" y1="24" x2="39" y2="24" style="stroke-width:2.5"/>
        <line class="icon-line" x1="10" y1="30" x2="38" y2="30" style="stroke-width:2.5"/>
      </svg>
      <span class="value">www.corvaneconseil.ch</span>
    </li>
    <li class="contact address">
      <svg class="icon" viewBox="0 0 48 48" aria-hidden="true">
        <path class="icon-fill" fill-rule="evenodd" d="M24 4c-9 0-16 7-16 15 0 10 16 27 16 27s16-17 16-27c0-8-7-15-16-15zm0 10a5 5 0 1 1 0 10 5 5 0 0 1 0-10z"/>
      </svg>
      <span class="value">Rue des Vergers-Bleus 14 1201 Genève</span>
    </li>
    <li class="contact email">
      <svg class="icon" viewBox="0 0 48 48" aria-hidden="true">
        <path class="icon-fill" d="M2 8h44v4L24 27 2 12z"/>
        <path class="icon-fill" d="M2 16l14 10L2 38zM46 16v22L32 26zM18 28l6 4 6-4 16 12H2z"/>
      </svg>
      <span class="value">tv@corvaneconseil.ch</span>
    </li>
  </ul>
</main>
</body>
</html>
```